Fern Assembly Business Cards

Looking or a business card design for my start-up, called "Fern Assembly".
Our tagline is "Unleashing the human potential for good through leadership, culture, and education."
Our mission-driven work includes professional/personal development workshops, educational design services, organizational & project management consulting, and coaching services for K-12 schools, organizations, and individuals.
You can check out the website we're building at fernassembly.example
I select projects from designers who are highly responsive to feedback, engage in dialog about revisions, and provide all root/source documents (so please state in your initial submission that you agree to do so).
Looking forward to seeing your great designs!!
Updates
Hello everyone,
Industry/Entity Type
Building
Requirements
Must have
- Looking for a two sided design that includes our logo (I am uploading two variations that I would like incorporated in .ai format) and website on both sides.
The front side must include:
Logo, Name, Title, Phone, Email, Twitter handle
The back side must include: Logo, @fernassem (our organizational twitter handle)
Nice to have
- I like the rounded corner business cards, but that is not absolutely essential.
Should not have
- Colors beyond those presented in our logo.

```html
<!DOCTYPE html>
<html lang="en">
<head>
<meta charset="utf-8">
<title>Fern Assembly Business Cards</title>
<link rel="stylesheet" href="https://fonts.googleapis.com/css2?family=Oswald:wght@500;600&display=swap">
<style>
  :root{
    --backdrop:#2a2a2b;
    --card-white:#ffffff;
    --card-mist:#e9ebee;
    --card-slate:#4b4b4e;
    --card-slate-deep:#3c3c3f;
    --brand-blue:#1d5fae;
    --brand-blue-deep:#14468a;
    --brand-sky:#6fc6d9;
    --brand-stone:#a59f97;
    --text-grey:#8c8a87;
    --text-light:#e8eef6;
  }
  *{margin:0;padding:0;box-sizing:border-box}
  html,body{width:1200px;height:900px;overflow:hidden;background:var(--backdrop)}
  .canvas{position:relative;width:1200px;height:900px;display:flex;flex-direction:column;align-items:center;justify-content:center;gap:44px}
  .card{position:relative;width:640px;height:366px;border-radius:10px;overflow:hidden;box-shadow:0 14px 36px rgba(0,0,0,.45)}
  .card-art{position:absolute;inset:0;width:100%;height:100%}

  .brand{position:absolute;display:flex;flex-direction:column;align-items:center}
  .brand-name{font-family:"Oswald",sans-serif;font-weight:500;font-size:30px;letter-spacing:2px;color:var(--text-grey);line-height:1.1}
  .brand-url{margin-top:6px;font-family:"Oswald",sans-serif;font-weight:500;font-size:11px;letter-spacing:1px;color:var(--text-grey)}

  /* front */
  .card-front{background:linear-gradient(160deg,var(--card-white) 40%,var(--card-mist))}
  .card-front .brand{top:66px;right:44px}
  .holder{position:absolute;top:70px;left:40px;font-family:"Oswald",sans-serif;color:var(--brand-blue)}
  .holder-name{font-size:26px;font-weight:600;line-height:1.1}
  .holder-title{font-size:15px;font-weight:500;letter-spacing:.3px}
  .contacts{position:absolute;left:40px;bottom:30px;list-style:none;font-family:"Oswald",sans-serif;font-weight:500;font-size:17px;letter-spacing:1.5px;color:var(--text-light)}
  .contacts li{display:flex;align-items:center;gap:16px;height:32px}
  .contact-icon{width:22px;height:22px;flex:none}
  .social-dot{width:14px;height:14px;margin:0 4px;border-radius:50%;background:var(--text-light);flex:none}

  /* back */
  .card-back{background:radial-gradient(ellipse at 40% 40%,var(--card-slate),var(--card-slate-deep))}
  .card-back .brand{top:140px;left:90px}
  .card-back .brand-name,.card-back .brand-url{color:var(--brand-stone)}
  .back-handle{position:absolute;right:46px;top:150px;display:flex;align-items:center;gap:10px;font-family:"Oswald",sans-serif;font-weight:500;font-size:16px;letter-spacing:1px;color:var(--text-light)}
  .back-handle .social-dot{margin:0}
</style>
</head>
<body>
<main class="canvas">

  <section class="card card-back" aria-label="Back of card">
    <svg class="card-art" viewBox="0 0 640 366" aria-hidden="true">
      <path d="M0 338 C170 312 280 262 330 190 C385 110 470 55 640 22" fill="none" stroke="var(--brand-stone)" stroke-width="4"/>
      <path d="M360 240 C420 140 500 70 640 36" fill="none" stroke="var(--brand-sky)" stroke-width="4"/>
    </svg>
    <div class="brand">
      <p class="brand-name">FERN ASSEMBLY</p>
      <p class="brand-url">www.fernassembly.example</p>
    </div>
    <p class="back-handle"><span class="social-dot"></span>@FERNASSEM</p>
  </section>

  <section class="card card-front" aria-label="Front of card">
    <svg class="card-art" viewBox="0 0 640 366" aria-hidden="true">
      <path d="M0 196 C160 150 320 200 430 186 C530 174 600 140 640 96" fill="none" stroke="var(--brand-stone)" stroke-width="7"/>
      <path d="M0 188 C150 170 260 172 330 174" fill="none" stroke="var(--brand-sky)" stroke-width="5"/>
      <path d="M0 212 C160 168 320 214 440 200 C540 188 610 156 640 120 L640 366 L0 366 Z" fill="var(--brand-sky)"/>
      <path d="M0 222 C160 180 320 224 440 212 C540 200 610 170 640 136 L640 366 L0 366 Z" fill="var(--brand-blue)"/>
      <path d="M0 250 C200 230 420 280 640 200 L640 366 L0 366 Z" fill="var(--brand-blue-deep)" opacity=".35"/>
    </svg>
    <div class="holder">
      <h1 class="holder-name">JORDAN VALE</h1>
      <p class="holder-title">GENERAL MANAGER</p>
    </div>
    <div class="brand">
      <p class="brand-name">FERN ASSEMBLY</p>
      <p class="brand-url">www.fernassembly.example</p>
    </div>
    <ul class="contacts">
      <li>
        <svg class="contact-icon" viewBox="0 0 22 22" aria-hidden="true"><rect x="6" y="2" width="10" height="18" rx="2" fill="none" stroke="var(--text-light)" stroke-width="1.6"/><rect x="8" y="5" width="6" height="7" fill="var(--text-light)"/></svg>
        +1 555-014-2270
      </li>
      <li>
        <svg class="contact-icon" viewBox="0 0 22 22" aria-hidden="true"><rect x="2" y="5" width="18" height="13" fill="none" stroke="var(--text-light)" stroke-width="1.6"/><path d="M2 5 L11 12 L20 5" fill="none" stroke="var(--text-light)" stroke-width="1.6"/></svg>
        HELLO@FERNASSEMBLY.EXAMPLE
      </li>
      <li><span class="social-dot"></span>@FERNASSEM</li>
    </ul>
  </section>

</main>
</body>
</html>
```